Denver-based business coaching & networking business needs marketing postcard design

We need help designing an oversized postcard that our sales team can use as a leave-behind when they are talking to different businesses and professionals. We have a program that has business owners and sales professionals attend a one day seminar to develop an executable business plan online that is ready to be implemented. Following the seminar they participate in bi-weekly group meetings where they collaborate with other professionals, review and stay accountable to their plan, and pass referrals. We would like to have a few graphics included from our website (www.velmaric.com) including the Shape-Launch-Gather graphic and the "Six Traps That Sink Ventures" graphic. The final design should be able to have a clear call-to-action about attending a seminar to begin their journey with Velmaric.

Language we would like to have included is as follows:

Learn Business Strategy
Create an Executable Business Plan
Receive Consistent Coaching
Attend Additional Educational Sessions
Profit from Peer Collaboration
Stay Accountable through Bi-Weekly Meetings
Increase your income through Referrals

The role of Velmaric is to develop successful business people through education, collaboration and community. This is created by first attending a one day seminar whose purpose is to assist attendees in creating an immediately executable business plan. Attendees then meet bi-weekly to pass referrals, collaborate on challenges and continually check in on their own plans, to ensure their continued success.

Target Market(s)

Age 28-45, Realtors, Mortgage Brokers, Insurance Professionals, Financial Advisors, CPA's, Attorneys, Small Business Owners

Industry/Entity Type

Business Consultant

Font styles to use
Sans Serif

Colors
faa54b
f37122

Requirements
Must have
• Velmaric logo, text that was provided in description, graphics that hit on elements from our website, call to action, website address

```html
<!DOCTYPE html>
<html lang="en">
<head>
<meta charset="utf-8">
<title>Velmaric Postcard</title>
<link rel="stylesheet" href="https://fonts.googleapis.com/css2?family=Arimo:ital,wght@0,400;0,700;1,400;1,700&family=Barlow+Condensed:ital,wght@1,500;1,700;1,800;1,900&family=Questrial&family=Parisienne&display=swap">
<style>
  :root {
    --orange-light: #faa54b;
    --orange: #f7943a;
    --orange-deep: #f37122;
    --orange-text: #d9691f;
    --grey-panel: #8c8c8c;
    --grey-box: #e6e6e6;
    --ink: #1c1c1c;
    --ink-soft: #555555;
    --paper: #ffffff;
    --pale-yellow: #f7efb2;
  }
  * { box-sizing: border-box; margin: 0; padding: 0; }
  html, body { width: 886px; height: 1200px; overflow: hidden; background: var(--paper); }
  body { position: relative; font-family: "Arimo", Arial, sans-serif; }

  .card {
    position: absolute; left: 44px; width: 798px; height: 516px; overflow: hidden;
    background: var(--paper);
    box-shadow: 0 2px 5px rgba(0,0,0,.35);
  }
  .card--front { top: 46px; }
  .card--back { top: 632px; }
  .card__shapes { position: absolute; inset: 0; width: 100%; height: 100%; }
  .abs { position: absolute; }

  /* front */
  .brand-block { left: 24px; top: 26px; }
  .brand-block__square { width: 74px; height: 74px; background: var(--orange); }
  .brand-block__name { margin-top: 14px; font-family: "Questrial", sans-serif; font-size: 24px; color: var(--ink-soft); letter-spacing: .5px; }

  .headline-top { right: 26px; top: 56px; font-family: "Barlow Condensed", sans-serif; font-style: italic; font-weight: 800; font-size: 34px; color: var(--ink); line-height: 1; }
  .headline-main { right: 26px; top: 82px; font-family: "Barlow Condensed", sans-serif; font-style: italic; font-weight: 900; font-size: 104px; color: var(--paper); line-height: 1; letter-spacing: 1px; }
  .headline-with { left: 406px; top: 166px; font-family: "Arimo", sans-serif; font-weight: 700; font-size: 30px; color: var(--paper); }
  .headline-brand { right: 26px; top: 172px; display: flex; align-items: center; gap: 10px; }
  .headline-brand__square { width: 40px; height: 40px; background: var(--ink); }
  .headline-brand__name { font-family: "Questrial", sans-serif; font-size: 48px; color: var(--ink); line-height: 1; }

  .benefits { right: 32px; top: 227px; list-style: none; }
  .benefits li { display: flex; justify-content: flex-end; align-items: center; height: 28.7px; gap: 12px; font-family: "Barlow Condensed", sans-serif; font-style: italic; font-weight: 700; font-size: 19px; color: var(--paper); }
  .benefits svg { width: 24px; height: 24px; flex: none; }

  .event-pill { left: 402px; top: 441px; width: 420px; height: 54px; border-radius: 27px 0 0 27px; background: linear-gradient(#ffffff 55%, #d9d9d9); padding: 8px 26px 0 0; text-align: right; }
  .event-pill__lead { font-family: "Barlow Condensed", sans-serif; font-style: italic; font-weight: 700; font-size: 15px; color: var(--ink); }
  .event-pill__url { font-weight: 700; font-size: 16px; color: var(--orange-deep); letter-spacing: .3px; }
  .event-pill__url span { color: var(--ink); font-size: 12px; margin-right: 4px; }

  /* back */
  .fail-title { left: 28px; top: 32px; font-style: italic; font-weight: 700; font-size: 16.5px; line-height: 1.25; color: var(--pale-yellow); letter-spacing: .3px; }
  .fail-list { left: 30px; top: 83px; list-style: none; }
  .fail-list li { display: flex; align-items: center; gap: 9px; height: 20.6px; font-family: "Barlow Condensed", sans-serif; font-style: italic; font-weight: 500; font-size: 14.5px; color: var(--paper); }
  .fail-list svg { width: 14px; height: 14px; flex: none; }

  .role-copy { right: 24px; top: 26px; width: 370px; text-align: right; color: var(--paper); }
  .role-copy__intro { font-style: italic; font-size: 12.6px; line-height: 1.25; }
  .role-copy__lead { margin-top: 5px; font-style: italic; font-weight: 700; font-size: 14.4px; line-height: 1.3; }
  .role-copy__tail { margin-top: 6px; font-style: italic; font-size: 12.6px; line-height: 1.25; }

  .approach-title { left: 0; width: 798px; top: 192px; text-align: center; font-family: "Questrial", sans-serif; font-size: 34px; color: var(--ink); letter-spacing: -.3px; }

  .step { left: 58px; display: flex; gap: 18px; }
  .step__icon { width: 50px; height: 50px; flex: none; margin-top: 4px; }
  .step__title { font-style: italic; font-weight: 700; font-size: 21px; color: var(--orange-text); line-height: 1; }
  .step__text { margin-top: 3px; font-size: 13px; line-height: 1.3; color: var(--paper); width: 310px; }
  .step-number { font-family: "Barlow Condensed", sans-serif; font-style: italic; font-weight: 500; font-size: 50px; color: var(--orange-deep); line-height: 1; }

  .cta-box { left: 470px; top: 252px; width: 304px; height: 240px; text-align: center; padding-top: 18px; padding-left: 24px; }
  .cta-box__title { font-family: "Barlow Condensed", sans-serif; font-weight: 700; font-style: normal; font-size: 30px; line-height: 1.1; color: var(--ink); }
  .cta-box__text { margin-top: 10px; font-size: 15px; line-height: 1.45; color: var(--ink); }
  .cta-box__register { margin-top: 6px; font-family: "Parisienne", cursive; font-size: 19px; color: var(--ink-soft); }
  .cta-box__url { margin-top: 8px; font-weight: 700; font-size: 16px; color: var(--orange-deep); letter-spacing: .3px; }
  .cta-box__brand { margin-top: 10px; display: inline-flex; align-items: center; gap: 5px; }
  .cta-box__brand-square { width: 14px; height: 14px; background: var(--ink); }
  .cta-box__brand-name { font-family: "Questrial", sans-serif; font-size: 18px; color: var(--ink); }
</style>
</head>
<body>

<!-- FRONT -->
<section class="card card--front">
  <svg class="card__shapes" viewBox="0 0 798 516" aria-hidden="false">
    <defs>
      <linearGradient id="photoTone" x1="0" y1="0" x2="1" y2="1">
        <stop offset="0" stop-color="#7a5a44"/>
        <stop offset=".55" stop-color="#c9c2bb"/>
        <stop offset="1" stop-color="#eeeeee"/>
      </linearGradient>
    </defs>
    <polygon points="798,0 523,0 285,255 333,516 798,516" fill="var(--orange)"/>
    <polygon points="285,255 333,516 420,516 360,300 470,170" fill="var(--orange-deep)"/>
    <polygon role="img" aria-label="Photo of a coach presenting at a whiteboard to seated attendees" points="251,0 523,0 285,255 333,516 0,516 0,368" fill="url(#photoTone)"/>
  </svg>

  <div class="abs brand-block">
    <div class="brand-block__square"></div>
    <div class="brand-block__name">VELMARIC</div>
  </div>

  <div class="abs headline-top">BRING YOUR BUSINESS</div>
  <div class="abs headline-main">TO LIFE</div>
  <div class="abs headline-with">with</div>
  <div class="abs headline-brand">
    <span class="headline-brand__square"></span>
    <span class="headline-brand__name">VELMARIC</span>
  </div>

  <ul class="abs benefits">
    <li>Learn Business Strategy<svg viewBox="0 0 24 24"><circle cx="12" cy="12" r="11" fill="#fff"/><circle cx="11" cy="11" r="4.5" fill="none" stroke="var(--orange)" stroke-width="2"/><line x1="14" y1="14" x2="18" y2="18" stroke="var(--orange)" stroke-width="2"/></svg></li>
    <li>Create an Executable Business Plan<svg viewBox="0 0 24 24"><circle cx="12" cy="12" r="11" fill="#fff"/><rect x="6.5" y="7" width="11" height="10" fill="none" stroke="var(--orange)" stroke-width="1.8"/><polyline points="6.5,7 12,12 17.5,7" fill="none" stroke="var(--orange)" stroke-width="1.5"/></svg></li>
    <li>Receive Consistent Coaching<svg viewBox="0 0 24 24"><circle cx="12" cy="12" r="11" fill="#fff"/><circle cx="9" cy="9" r="2.3" fill="var(--orange)"/><circle cx="15" cy="9" r="2.3" fill="var(--orange)"/><rect x="6" y="12.5" width="12" height="5" rx="2" fill="var(--orange)"/></svg></li>
    <li>Attend Additional Educational Sessions<svg viewBox="0 0 24 24"><circle cx="12" cy="12" r="11" fill="#fff"/><rect x="7.5" y="6" width="9" height="12" fill="none" stroke="var(--orange)" stroke-width="1.8"/><line x1="9.5" y1="10" x2="14.5" y2="10" stroke="var(--orange)" stroke-width="1.4"/><line x1="9.5" y1="13" x2="14.5" y2="13" stroke="var(--orange)" stroke-width="1.4"/></svg></li>
    <li>Profit from Peer Collaboration<svg viewBox="0 0 24 24"><circle cx="12" cy="12" r="11" fill="#fff"/><circle cx="8" cy="10" r="2.2" fill="var(--orange)"/><circle cx="12" cy="8.5" r="2.4" fill="var(--orange)"/><circle cx="16" cy="10" r="2.2" fill="var(--orange)"/><rect x="6" y="12.5" width="12" height="5" rx="2.5" fill="var(--orange)"/></svg></li>
    <li>Stay Accountable through Bi-Weekly Meetings<svg viewBox="0 0 24 24"><circle cx="12" cy="12" r="11" fill="#fff"/><path d="M5.5 12 L9 9 L12 11 L15 9 L18.5 12 L13 16 Z" fill="none" stroke="var(--orange)" stroke-width="1.6" stroke-linejoin="round"/></svg></li>
    <li>Increase your income through Referrals<svg viewBox="0 0 24 24"><circle cx="12" cy="12" r="11" fill="#fff"/><rect x="7" y="13" width="2.5" height="4" fill="var(--orange)"/><rect x="10.8" y="11" width="2.5" height="6" fill="var(--orange)"/><rect x="14.6" y="9" width="2.5" height="8" fill="var(--orange)"/><polyline points="7,11 11,8 16,6" fill="none" stroke="var(--orange)" stroke-width="1.4"/></svg></li>
  </ul>

  <div class="abs event-pill">
    <div class="event-pill__lead">Attend our next Live Event and begin your journey with Velmaric</div>
    <div class="event-pill__url"><span>@</span>WWW.VELMARIC.COM</div>
  </div>
</section>

<!-- BACK -->
<section class="card card--back">
  <svg class="card__shapes" viewBox="0 0 798 516">
    <rect x="0" y="0" width="798" height="182" fill="var(--grey-panel)"/>
    <polygon points="437,0 798,0 798,182 389,182" fill="var(--orange-deep)"/>
    <polygon points="0,240 454,240 528,516 0,516" fill="var(--orange)"/>
    <!-- growth chart -->
    <g fill="none" stroke="#fff" stroke-width="1.8">
      <rect x="274" y="154" width="14" height="10"/>
      <rect x="292" y="149" width="14" height="15"/>
      <rect x="310" y="141" width="14" height="23"/>
      <rect x="328" y="131" width="14" height="33"/>
      <rect x="346" y="117" width="14" height="47"/>
      <rect x="364" y="102" width="14" height="62"/>
      <rect x="382" y="84" width="14" height="80"/>
      <path d="M276 150 C 340 140, 390 110, 398 44"/>
    </g>
    <ellipse role="img" aria-label="Photo of a hand pointing to the top of the chart" cx="423" cy="66" rx="18" ry="14" fill="#d9b8a0" opacity=".85"/>
    <!-- CTA frame -->
    <polygon points="470,252 774,252 774,492 536,492" fill="var(--grey-box)" stroke="var(--orange)" stroke-width="3"/>
  </svg>

  <div class="abs fail-title">The typical business plan<br>fails for one of four reasons:</div>
  <ul class="abs fail-list">
    <li><svg viewBox="0 0 14 14"><path d="M2 3 H9 L12 7 L9 11 H6" fill="none" stroke="#fff" stroke-width="1.4"/></svg>There are too many goals</li>
    <li><svg viewBox="0 0 14 14"><path d="M1 3 H5 L6.5 4.5 H13 V12 H1 Z" fill="#fff"/></svg>It's filed away; never to be seen again</li>
    <li><svg viewBox="0 0 14 14"><rect x="1" y="10" width="2" height="3" fill="#fff"/><rect x="4.5" y="8" width="2" height="5" fill="#fff"/><rect x="8" y="5" width="2" height="8" fill="#fff"/><rect x="11.5" y="2" width="2" height="11" fill="#fff"/></svg>There are no metrics to measure success</li>
    <li><svg viewBox="0 0 14 14"><circle cx="7" cy="7" r="5.6" fill="none" stroke="#fff" stroke-width="1.4"/><polyline points="7,3.5 7,7 9.5,8.5" fill="none" stroke="#fff" stroke-width="1.4"/></svg>There is no timetable or accountability</li>
  </ul>

  <div class="abs role-copy">
    <p class="role-copy__intro">The role of Velmaric is to develop successful business people through education, collaboration and community.</p>
    <p class="role-copy__lead">This is created by first attending a one day seminar whose purpose is to assist attendees in creating an immediately executable business plan.</p>
    <p class="role-copy__tail">Attendees then meet bi-weekly to pass referrals, collaborate on challenges and continually check in on their own plans, to ensure their continued success.</p>
  </div>

  <div class="abs approach-title">Velmaric offers a three-pronged approach</div>

  <div class="abs step" style="top:258px">
    <svg class="step__icon" viewBox="0 0 50 50"><circle cx="25" cy="25" r="25" fill="#fff"/><polygon points="25,15 42,22 25,29 8,22" fill="var(--orange)"/><path d="M15 25 V32 C20 36 30 36 35 32 V25 L25 29 Z" fill="var(--orange)"/></svg>
    <div><div class="step__title">Shape</div><p class="step__text">Map out a strategic path for your business at one of our interactive, one-day seminars.</p></div>
  </div>
  <div class="abs step" style="top:336px">
    <svg class="step__icon" viewBox="0 0 50 50"><circle cx="25" cy="25" r="25" fill="#fff"/><line x1="15" y1="36" x2="29" y2="22" stroke="var(--orange)" stroke-width="5" stroke-linecap="round"/><circle cx="32" cy="19" r="7" fill="var(--orange)"/><circle cx="35" cy="16" r="3.5" fill="#fff"/></svg>
    <div><div class="step__title">Launch</div><p class="step__text">Continue your development with a customized, ongoing educational package.</p></div>
  </div>
  <div class="abs step" style="top:410px">
    <svg class="step__icon" viewBox="0 0 50 50"><circle cx="25" cy="25" r="25" fill="#fff"/><circle cx="21" cy="19" r="6" fill="var(--orange)"/><path d="M10 36 C10 28 32 28 32 36 Z" fill="var(--orange)"/><path d="M33 28 L41 36 M41 28 L33 36" stroke="var(--orange)" stroke-width="2.6"/></svg>
    <div><div class="step__title">Gather</div><p class="step__text">Engage with and be held accountable by your peers in the Velmaric community while honing your skills for continued success</p></div>
  </div>

  <div class="abs step-number" style="left:418px;top:272px">1</div>
  <div class="abs step-number" style="left:436px;top:346px">2</div>
  <div class="abs step-number" style="left:456px;top:424px">3</div>

  <div class="abs cta-box">
    <div class="cta-box__title">Ready To Build<br>A Better Business?</div>
    <p class="cta-box__text">Attend our next Live Event to<br>begin your journey with Velmaric</p>
    <div class="cta-box__register">Register at:</div>
    <div class="cta-box__url">WWW.VELMARIC.COM</div>
    <div class="cta-box__brand"><span class="cta-box__brand-square"></span><span class="cta-box__brand-name">VELMARIC</span></div>
  </div>
</section>

</body>
</html>
```